Come crowdsource a Web Design for a brazilian crowdsource Startup!

> NAME OF OUR STARTUP:
Mundaleo

> DESCRIPTION OF OUR STARTUP:
We are a crowdsourcing startup in Brazil providing consultancy and technology to support other companies to crowdsource their projects.
We also operate doing big crowdsource campaings related to polemic subjects in Brazil.

> WHAT ARE OUR TARGET AUDIENCE?
Our target audience are young people around 20-35 years old.
Generation Y (Millennial Generation)

> WHAT IS OUR INDUSTRY?
Internet, web

> WHAT DO WE NEED?
We need a Web Design for our first site.

We need 5 pages:
- Home
- What is Crowdsourcing?
- Solutions
- About Us
- Blog
- A box for the "Contact" tab (this is not a page)

Please, find attached a Layout Sketch of what I've imagined.

Lets talk about the sketch:
Well, first of all, it's a SKETCH, so you don't have to send proposals exactly as the sketch. The sketch is just to show how I've imagined the ditribution of the content boxes. For example, the menu bar doesnt need to be a rectangle exactly like the sketch, but, I would like to have the menu on the right side of the logo. Also, you will see that the boxes are all squeezed, of course I dont want them soo squeezed! Again, its juust a SKETCH!

About the images on the sketch:
IMG1 - Some nice and simple image related to collectivity or related to crowdsourcing or maybe use our O logo.

IMG2 - Some simple and creative image related to Consultancy. It doesnt need to be so obvious.

IMG3 - Some simple and creative image related to Web 2.0 Software Technology. It doesnt need to be so obvious.

IMG4 - Some simple and creative image related to a full package of Consultancy + Technology. It doesnt need to be so obvious.

IMG5 - Some nice and simple image related to collectivity or related to crowdsourcing.

IMG6 - Some nice and simple image related to Ideation. Maybe a light bulb? I dont know, be creative!

IMG7 - Some nice and simple image related to Crowdlabor. I dont know, be creative!

IMG8 - Some nice and simple image related to CrowdFeedback. Maybe a megaphone? A loudspeaker? I dont know, be creative!

IMG9 - Some nice and simple image related to us! Maybe our O logo ? I dont know, be creative!

THE CONTACT SIDE BAR - we need a nice and simple contact side bar. By the way, on the sketch this bar is shown only at the homepage, but when the site becomes real this bar will stay along all the pages.

THE CONTACT BOX - we need a nice and simple contact box.

ABOUT THE COLORS TO USE: we would like some color to our background and titles. We like colors similars to our logo: really light blue ? light green/blue ? light grey ? light orange ? I dont know, you guys knows more about that then me =)

CHATTERBOX SHARE/LIKE BUTTON: We would like a chatterbox share/like button somewhere on the site!

ABOUT THE ATTACHED FILES:

ADDITIONALS:
> The name Mundaleo comes from "collectivity". With our name we want to pass the idea of the collectivity from the crowdsource work model.

> Our communication is directed to the Generation Y.

> Remember, we are a Startup! So we need a modern and simple site, something like the web 2.0 trends. It must be beautiful =)

> We arent a serious company. We are a young and fun company! Please, dont come with old fashionable company sites.

> Be creative =] !

Target Market(s)

Our target audience are young people around 20-35 years old. Generation Y (Millennial Generation)

Industry/Entity Type

Communication

Requirements
Must have
• We need a Web Design for our first site.

We need 5 pages:
- Home
- What is Crowdsourcing?
- Solutions
- About Us
- Blog

ABOUT THE COLORS TO USE: we would like some color to our background and titles. We like colors similars to our logo: really light blue ? light green/blue ? light grey ? light oranges ? I dont know, you guys knows more about that then me =)

Should not have
• Poor/serious/old fashionable designs

```html
<!DOCTYPE html>
<html lang="en">
<head>
<meta charset="utf-8">
<title>Mundaleo – What Is Crowdsourcing</title>
<link rel="stylesheet" href="https://fonts.googleapis.com/css2?family=Source+Sans+3:ital,wght@0,400;0,600;0,700;1,700&display=swap">
<style>
  :root {
    --teal-dark: #137f8a;
    --teal: #1d8a93;
    --sky-light: #c8e9ef;
    --sky: #8fd0dc;
    --hole: #b9e2ea;
    --paper: #ffffff;
    --ink: #111111;
    --text: #555555;
    --orange: #f0901e;
    --yellow: #f5c518;
    --red: #e3262b;
    --footer: #333333;
    --tape: rgba(250, 226, 140, 0.8);
  }
  * { box-sizing: border-box; margin: 0; padding: 0; }
  html, body { width: 1113px; height: 1200px; overflow: hidden; }
  body {
    position: relative;
    font-family: "Source Sans 3", sans-serif;
    background: var(--sky);
    color: var(--text);
  }
  .backdrop-band {
    position: absolute; left: 0; top: 122px; width: 1113px; height: 544px;
    background-color: var(--sky-light);
    background-image:
      linear-gradient(rgba(255,255,255,0.35) 1px, transparent 1px),
      linear-gradient(90deg, rgba(255,255,255,0.35) 1px, transparent 1px);
    background-size: 8px 8px;
  }
  .site-header {
    position: absolute; left: 0; top: 0; width: 1113px; height: 122px;
    background: var(--teal-dark);
    border-bottom: 2px solid #0e6870;
  }
  .brand {
    position: absolute; left: 40px; top: 28px;
    display: flex; align-items: center; gap: 12px;
    font-size: 52px; font-weight: 700; color: #ffffff; line-height: 1;
  }
  .brand-dot { width: 40px; height: 40px; border-radius: 50%; background: var(--yellow); }
  .main-nav { position: absolute; top: 44px; left: 0; width: 1113px; }
  .main-nav a {
    position: absolute; font-size: 22px; font-weight: 600; color: #ffffff;
    text-decoration: none; white-space: nowrap;
  }
  .main-nav a.is-current { color: var(--orange); }
  .paper {
    position: absolute; left: 44px; top: 153px; width: 1027px; height: 963px;
    background: var(--paper);
    box-shadow: 0 6px 10px rgba(0,0,0,0.25);
  }
  .punch-holes { position: absolute; left: 0; top: 0; }
  .feature-photo {
    position: absolute; left: 63px; top: 256px; width: 441px; height: 286px;
    background: #ffffff; transform: rotate(-0.8deg);
    box-shadow: 0 2px 6px rgba(0,0,0,0.35);
  }
  .feature-photo .art {
    position: absolute; left: 10px; top: 11px; right: 10px; bottom: 11px;
    background: linear-gradient(100deg, #b7e3ea 0%, #e8a98a 45%, #f6b48e 70%, #b7e3ea 100%);
  }
  .tape {
    position: absolute; left: 186px; top: 240px; width: 205px; height: 38px;
    background: var(--tape); transform: rotate(-1deg);
  }
  .intro { position: absolute; left: 525px; top: 286px; width: 502px; }
  .section-title { font-size: 23px; font-weight: 600; color: var(--ink); }
  .section-title .accent { color: var(--teal); }
  .intro p {
    margin-top: 12px; font-size: 14px; line-height: 18px; text-align: justify;
  }
  .intro p + p { margin-top: 18px; }
  .uses-title {
    position: absolute; left: 0; top: 618px; width: 1113px; text-align: center;
  }
  .use-card { position: absolute; top: 688px; width: 300px; text-align: center; }
  .use-card .badge { display: block; margin: 0 auto; }
  .use-card h3 {
    margin-top: 38px; font-size: 25px; font-weight: 600; color: var(--ink);
  }
  .use-card p {
    margin: 8px auto 0; width: 290px; font-size: 12.2px; line-height: 15.8px; color: #333333;
  }
  .use-card .learn-more {
    display: inline-block; font-size: 12px; font-weight: 700; font-style: italic;
    color: var(--yellow); text-decoration: none;
  }
  .share-tab {
    position: absolute; left: 1066px; top: 340px; width: 47px; height: 66px;
    background: var(--teal-dark); color: #ffffff; text-align: center;
    font-size: 14px; font-weight: 700; padding-top: 4px;
  }
  .share-tab .share-mark {
    display: block; width: 24px; height: 24px; margin: 6px auto 0;
    border-radius: 50%; background: #5bb6c0;
  }
  .contact-tab {
    position: absolute; left: 1066px; top: 414px; width: 47px; height: 141px;
    background: var(--red); border: 2px solid #ffffff; border-right: 0;
  }
  .contact-tab span {
    position: absolute; left: 50%; top: 50%;
    transform: translate(-50%, -50%) rotate(-90deg);
    white-space: nowrap; color: #ffffff; font-size: 19px; font-weight: 600;
  }
  .site-footer {
    position: absolute; left: 0; top: 1152px; width: 1113px; height: 48px;
    background: var(--footer); color: #ffffff; font-size: 12px;
    text-align: center; line-height: 48px;
  }
</style>
</head>
<body>
  <div class="backdrop-band"></div>

  <header class="site-header">
    <div class="brand"><span class="brand-dot"></span>Mundaleo</div>
    <nav class="main-nav">
      <a class="is-current" href="#" style="left:517px">What Is Crowdsourcing</a>
      <a href="#" style="left:775px">Solutions</a>
      <a href="#" style="left:901px">About Us</a>
      <a href="#" style="left:1027px">Blog</a>
    </nav>
  </header>

  <main class="paper">
    <svg class="punch-holes" width="1027" height="40" viewBox="0 0 1027 40" aria-hidden="true">
      <g fill="var(--hole)">
        <circle cx="23" cy="22" r="14"/><circle cx="88" cy="22" r="14"/>
        <circle cx="154" cy="22" r="14"/><circle cx="219" cy="22" r="14"/>
        <circle cx="285" cy="22" r="14"/><circle cx="350" cy="22" r="14"/>
        <circle cx="416" cy="22" r="14"/><circle cx="481" cy="22" r="14"/>
        <circle cx="547" cy="22" r="14"/><circle cx="612" cy="22" r="14"/>
        <circle cx="678" cy="22" r="14"/><circle cx="743" cy="22" r="14"/>
        <circle cx="809" cy="22" r="14"/><circle cx="874" cy="22" r="14"/>
        <circle cx="940" cy="22" r="14"/><circle cx="1005" cy="22" r="14"/>
      </g>
    </svg>
  </main>

  <figure class="feature-photo">
    <div class="art" role="img" aria-label="Illustration of a curious person beside a red question-mark speech bubble"></div>
  </figure>
  <div class="tape"></div>

  <section class="intro">
    <h2 class="section-title">But, What is <span class="accent">Crowdsourcing ?</span></h2>
    <p>Crowdsourcing is the practice of obtaining needed services, ideas, or content by soliciting contributions from a large group of people, and especially from an online community, rather than from traditional employees or suppliers. Often used to subdivide tedious work or to fund-raise startup companies and charities, this process can occur both online and offline.</p>
    <p>The general concept is to combine the efforts of crowds of volunteers or part-time workers, where each one could contribute a small portion, which adds into a relatively large or significant result.</p>
  </section>

  <h2 class="section-title uses-title">Some uses of <span class="accent">Crowdsourcing</span></h2>

  <article class="use-card" style="left:79px">
    <svg class="badge" width="216" height="216" viewBox="0 0 216 216" role="img" aria-label="Ideation illustration: a lightbulb filled with colourful idea dots">
      <defs><radialGradient id="g-ideation"><stop offset="0" stop-color="#f7d35a"/><stop offset="1" stop-color="#3fa9b8"/></radialGradient></defs>
      <circle cx="108" cy="108" r="100" fill="url(#g-ideation)" stroke="var(--orange)" stroke-width="10"/>
    </svg>
    <h3>Ideation</h3>
    <p>Crowdsourcing is the process of getting work or funding, usually online, from a crowd of people. The word is a combination of the words 'crowd' and 'outsourcing'. The idea is to take work and outsource it to a crowd of workers.<br><a class="learn-more" href="#">Learn More</a></p>
  </article>

  <article class="use-card" style="left:406px">
    <svg class="badge" width="216" height="216" viewBox="0 0 216 216" role="img" aria-label="Crowdlabor illustration: a smiling crowd of workers with a speech bubble">
      <defs><radialGradient id="g-labor"><stop offset="0" stop-color="#f6b48e"/><stop offset="1" stop-color="#e8643a"/></radialGradient></defs>
      <circle cx="108" cy="108" r="100" fill="url(#g-labor)" stroke="var(--orange)" stroke-width="10"/>
    </svg>
    <h3>Crowdlabor</h3>
    <p>Crowdsourcing is the process of getting work or funding, usually online, from a crowd of people. The word is a combination of the words 'crowd' and 'outsourcing'. The idea is to take work and outsource it to a crowd of workers.<br><a class="learn-more" href="#">Learn More</a></p>
  </article>

  <article class="use-card" style="left:734px">
    <svg class="badge" width="216" height="216" viewBox="0 0 216 216" role="img" aria-label="CrowdFeedback illustration: megaphones with a colourful speech bubble">
      <defs><radialGradient id="g-feedback"><stop offset="0" stop-color="#ffffff"/><stop offset="1" stop-color="#a9a9a9"/></radialGradient></defs>
      <circle cx="108" cy="108" r="100" fill="url(#g-feedback)" stroke="var(--orange)" stroke-width="10"/>
    </svg>
    <h3>CrowdFeedback</h3>
    <p>Crowdsourcing is the process of getting work or funding, usually online, from a crowd of people. The word is a combination of the words 'crowd' and 'outsourcing'. The idea is to take work and outsource it to a crowd of workers.<br><a class="learn-more" href="#">Learn More</a></p>
  </article>

  <aside class="share-tab" aria-label="Share on chatterbox">share<span class="share-mark"></span></aside>
  <aside class="contact-tab"><span>Contact Us</span></aside>

  <footer class="site-footer">Copyright 2013 Mundaleo. All Rights Reserved.</footer>
</body>
</html>
```